Business cards/stationary for physician office
Using existing logo
Bright & Fun-filled
Paul Verner, M.D.
Radiologist
Cedarpoint Imaging, LLC.
48 Quill Ridge Lane
Montgomery, TX 77490
office@brakwell-mail.net
www.cedarpointimaging-demo.com
Will contact the winning designer with actual contact info to replace above text. Please not website has not been updated with new logo, so make sure to use provided logo files.
Logo files
Logo file horizontal

```html
<!DOCTYPE html>
<html lang="en">
<head>
<meta charset="utf-8">
<title>Cedarpoint Imaging Stationery</title>
<link href="https://fonts.googleapis.com/css2?family=Cinzel:wght@600&family=Open+Sans:wght@400;600&display=swap" rel="stylesheet">
<style>
:root{
  --stage:#3b3c3e;
  --stage-dark:#2e2f31;
  --paper:#ffffff;
  --blue:#2f5f9e;
  --blue-dark:#234a7c;
  --grey:#c9ccd1;
  --ink:#3a4350;
  --muted:#8a9098;
  --label:#b9bcc0;
}
*{margin:0;padding:0;box-sizing:border-box}
html,body{width:1200px;height:382px;overflow:hidden}
body{background:radial-gradient(ellipse at 40% 40%,var(--stage),var(--stage-dark));position:relative;font-family:"Open Sans",sans-serif;color:var(--ink)}
.brand{position:absolute;display:flex;align-items:center;gap:6px}
.brand .dot{border-radius:50%;background:var(--blue);flex:none}
.brand .name{font-family:"Cinzel",serif;font-weight:600;line-height:1.05;letter-spacing:.04em;white-space:nowrap}
.hero-brand{left:60px;top:70px;gap:8px}
.hero-brand .dot{width:46px;height:46px;background:#fff}
.hero-brand .name{color:#fff;font-size:22px}
.card{position:absolute;width:138px;height:62px;background:var(--paper);box-shadow:0 2px 5px rgba(0,0,0,.5);overflow:hidden}
.card.blue{background:var(--blue)}
.card .brand .dot{width:12px;height:12px}
.card .brand .name{font-size:6px;color:var(--blue)}
.card .brand.front{left:38px;top:24px}
.card .brand.front .dot{width:14px;height:14px}
.card .brand.front .name{font-size:7px}
.card .brand.back{left:7px;top:7px}
.card .contact{position:absolute;left:76px;top:7px;font-size:3.6px;color:var(--muted);line-height:1.55;white-space:nowrap}
.card .band{position:absolute;left:0;right:0;bottom:0;background:var(--blue)}
.label{position:absolute;font-size:5px;color:var(--label);white-space:nowrap}
.sheet{position:absolute;top:22px;width:180px;height:236px;background:var(--paper);box-shadow:0 2px 6px rgba(0,0,0,.5);overflow:hidden}
.sheet .brand{left:12px;top:12px}
.sheet .brand .dot{width:16px;height:16px}
.sheet .brand .name{font-size:7.5px;color:var(--blue)}
.sheet .contact{position:absolute;left:124px;top:12px;font-size:3.6px;line-height:1.6;color:var(--muted);white-space:nowrap}
.sheet .footer-text{position:absolute;left:0;right:0;bottom:14px;text-align:center;font-size:3.6px;color:var(--muted)}
.sheet svg,.envelope svg{position:absolute;left:0;bottom:0}
.envelope{position:absolute;left:782px;width:394px;background:var(--paper);box-shadow:0 2px 6px rgba(0,0,0,.5);overflow:hidden}
.envelope .brand .dot{width:16px;height:16px}
.envelope .brand .name{font-size:8px;color:var(--blue)}
</style>
</head>
<body>

<div class="brand hero-brand"><span class="dot"></span><span class="name">Cedarpoint<br>Imaging</span></div>

<!-- business cards -->
<div class="card" style="left:24px;top:151px">
  <div class="brand front"><span class="dot"></span><span class="name">Cedarpoint<br>Imaging</span></div>
  <div class="band" style="height:4px"></div>
</div>
<div class="card" style="left:166px;top:151px">
  <div class="brand back"><span class="dot"></span><span class="name">Cedarpoint<br>Imaging</span></div>
  <div class="contact">Paul Verner, M.D.<br>Radiologist<br>48 Quill Ridge Lane<br>Montgomery, TX 77490<br>office@brakwell-mail.net<br>www.cedarpointimaging-demo.com</div>
  <div class="band" style="height:4px"></div>
</div>
<span class="label" style="left:48px;top:217px">CedarpointImaging_01_17526.ai</span>
<span class="label" style="left:200px;top:217px">CedarpointImaging_01_17526.ai</span>

<div class="card blue" style="left:24px;top:233px">
  <div class="brand front"><span class="dot" style="background:#fff"></span><span class="name" style="color:#fff">Cedarpoint<br>Imaging</span></div>
</div>
<div class="card" style="left:166px;top:233px">
  <div class="brand back"><span class="dot"></span><span class="name">Cedarpoint<br>Imaging</span></div>
  <div class="contact">Paul Verner, M.D.<br>Radiologist<br>48 Quill Ridge Lane<br>Montgomery, TX 77490<br>office@brakwell-mail.net<br>www.cedarpointimaging-demo.com</div>
  <div class="band" style="height:10px"></div>
</div>
<span class="label" style="left:48px;top:300px">CedarpointImaging_02_17527.ai</span>
<span class="label" style="left:200px;top:300px">CedarpointImaging_02_17527.ai</span>

<!-- letterheads -->
<div class="sheet" style="left:336px">
  <div class="brand"><span class="dot"></span><span class="name">Cedarpoint<br>Imaging</span></div>
  <div class="contact">48 Quill Ridge Lane<br>Montgomery, TX 77490<br>office@brakwell-mail.net</div>
  <div class="footer-text">www.cedarpointimaging-demo.com</div>
  <svg width="180" height="12" viewBox="0 0 180 12"><path d="M0 12V6Q90 0 180 4V12Z" fill="var(--grey)"/><path d="M0 12V9Q90 4 180 7V12Z" fill="var(--blue)"/></svg>
</div>
<span class="label" style="left:390px;top:262px">CedarpointImaging_01_17526.ai</span>

<div class="sheet" style="left:576px">
  <div class="brand"><span class="dot"></span><span class="name">Cedarpoint<br>Imaging</span></div>
  <div class="contact">48 Quill Ridge Lane<br>Montgomery, TX 77490<br>office@brakwell-mail.net</div>
  <div class="footer-text">www.cedarpointimaging-demo.com</div>
  <svg width="180" height="12" viewBox="0 0 180 12"><path d="M0 12V6Q90 0 180 4V12Z" fill="var(--grey)"/><path d="M0 12V9Q90 4 180 7V12Z" fill="var(--blue)"/></svg>
</div>
<span class="label" style="left:630px;top:262px">CedarpointImaging_02_17527.ai</span>

<!-- envelopes -->
<div class="envelope" style="top:22px;height:104px;background:#eef0f2">
  <svg width="394" height="104" viewBox="0 0 394 104"><path d="M0 0L197 60L394 0V18L197 74L0 18Z" fill="var(--grey)"/><path d="M0 84Q197 70 394 84V104H0Z" fill="var(--blue)"/></svg>
</div>
<div class="envelope" style="top:140px;height:86px">
  <div class="brand" style="left:14px;top:10px"><span class="dot"></span><span class="name">Cedarpoint<br>Imaging</span></div>
  <svg width="394" height="14" viewBox="0 0 394 14"><path d="M0 14V8Q197 0 394 6V14Z" fill="var(--grey)"/><path d="M0 14V11Q197 5 394 9V14Z" fill="var(--blue)"/></svg>
</div>
<div class="envelope" style="top:240px;height:58px;background:#eef0f2">
  <svg width="394" height="58" viewBox="0 0 394 58"><path d="M0 0L197 36L394 0Z" fill="var(--grey)"/></svg>
</div>
<div class="envelope" style="top:302px;height:58px">
  <div class="brand" style="left:186px;top:12px"><span class="dot"></span><span class="name">Cedarpoint<br>Imaging</span></div>
  <svg width="394" height="10" viewBox="0 0 394 10"><path d="M0 10V5Q197 0 394 4V10Z" fill="var(--blue)"/></svg>
</div>

</body>
</html>
```